Elegant wordpress web page for wedding rental of hand sanitizers

We want to rent our hand sanitizing towers out for high-end weddings. We need a very elegant, sophisticated page that describes our offering. You can see an ugly first draft here: trelvo.com/weddings
Target Market(s)
Wedding planners, wedding parents
Number of Pages Required
1 page
Font styles to use
Serif
Script
Colors
Designer to choose colors to be used in the design.
Requirements
Nice to have
- Two wedding-related sites for inspiration: quietorchardweddings-dot-com and fernlaneservices-dot-com

```html
<!DOCTYPE html>
<html lang="en">
<head>
<meta charset="utf-8">
<title>Trelvo – Wedding Hand Sanitizer Rental</title>
<link href="https://fonts.googleapis.com/css2?family=Playfair+Display:wght@700&family=Poppins:wght@400;500;600;700&display=swap" rel="stylesheet">
<style>
:root{
  --teal:#27c2cf;
  --blue:#0a93cf;
  --grad:linear-gradient(90deg,#2cc9cf,#0a95cd);
  --ink:#111417;
  --muted:#6f7479;
  --ice:#dff4f8;
  --line:#e6e9ec;
  --white:#fff;
}
*{margin:0;padding:0;box-sizing:border-box}
html,body{width:1200px;height:4559px;overflow:hidden}
body{font-family:'Poppins',sans-serif;color:var(--ink);background:var(--white);position:relative}
.abs{position:absolute}
.serif{font-family:'Playfair Display',serif;font-weight:700}
.btn{position:absolute;display:flex;align-items:center;justify-content:center;background:var(--grad);color:#fff;font-weight:600;border-radius:30px;font-size:14px;text-transform:uppercase;letter-spacing:.2px;box-shadow:0 4px 10px rgba(10,147,207,.25)}
.photo{position:absolute}

/* header */
.topline{position:absolute;left:0;top:0;width:1200px;height:4px;background:var(--teal)}
.brand{position:absolute;display:flex;align-items:center;gap:10px;font-weight:600;color:var(--blue)}
.brand .dot{border-radius:50%;background:var(--teal)}
.nav{position:absolute;left:338px;top:52px;display:flex;gap:24px;font-size:16px;font-weight:600;text-transform:uppercase}

/* hero */
.hero-box{position:absolute;left:549px;top:253px;width:534px;height:340px;background:rgba(255,255,255,.42);border-radius:8px;padding:40px 46px}
.hero-box h1{font-size:44px;line-height:62px;color:#141414}
.dots{position:absolute;left:573px;top:698px;display:flex;gap:4px}
.dots span{width:8px;height:8px;border-radius:50%;background:var(--blue)}
.dots span.on{background:#fff}

/* section headings */
.sec-title{position:absolute;left:0;width:1200px;text-align:center;font-size:42px}
.lede{position:absolute;left:140px;width:920px;text-align:center;font-size:13.5px;line-height:24px;color:var(--muted)}

/* about cards */
.card{position:absolute;top:942px;width:300px;height:329px;border:1px solid var(--line);border-radius:8px;background:#fff;padding:46px 30px 0 48px;box-shadow:0 2px 10px rgba(0,0,0,.05)}
.card.hot{background:linear-gradient(180deg,#2ecacf,#0a96cd);border:none;color:#fff}
.card h3{font-size:14px;font-weight:600;text-transform:uppercase;line-height:20px;margin-left:26px;margin-bottom:24px;position:relative}
.card h3 svg{position:absolute;left:-50px;top:-2px}
.card p{font-size:13.5px;line-height:20px;margin-bottom:10px;padding-right:8px}
.card.hot p{color:#e9fbff}

/* features */
.features{position:absolute;left:0;top:1349px;width:1200px;height:527px;background:linear-gradient(135deg,#e8eceb,#f4f1ee 40%,#e9eef0 70%,#ece6e3)}
.feat-img{position:absolute;left:535px;top:1558px;width:116px;height:318px;background:linear-gradient(180deg,#6a7f78,#b7a6a1 60%,#f2f2f2 61%,#fafafa);border-radius:4px}
.feat{position:absolute;display:flex;align-items:center;gap:18px;font-size:13.5px;font-weight:600;line-height:24px}
.feat.l{flex-direction:row-reverse;text-align:right}
.ico{width:46px;height:46px;border-radius:50%;background:var(--grad);display:flex;align-items:center;justify-content:center;flex:none;box-shadow:0 3px 8px rgba(10,147,207,.3)}

/* services */
.row-bg{position:absolute;left:0;width:1200px;height:525px;background:var(--ice)}
.svc{position:absolute;width:625px;background:#fff;border-radius:6px;padding:44px 32px 0;box-shadow:0 4px 18px rgba(0,0,0,.08)}
.svc h2{font-size:19px;font-weight:700;text-transform:uppercase;line-height:29px;margin-bottom:12px}
.svc p{font-size:14px;line-height:22px;color:var(--muted);margin-bottom:12px}
.svc ul{list-style:none;margin-bottom:22px}
.svc li{font-size:14px;line-height:23px;color:var(--muted);padding-left:16px;position:relative;margin-bottom:3px}
.svc li::before{content:"";position:absolute;left:0;top:9px;width:6px;height:6px;border-radius:50%;background:var(--teal)}
.svc .btn{position:static;display:inline-flex;height:38px;padding:0 23px;font-size:13.5px}

/* footer */
.f-head{position:absolute;top:4289px;font-size:22px;color:var(--teal)}
.sitemap{position:absolute;left:421px;top:4340px;list-style:none}
.sitemap li{font-size:15px;line-height:27px;padding-left:23px;position:relative}
.sitemap li::before{content:"";position:absolute;left:0;top:10px;width:7px;height:7px;border-radius:50%;background:var(--teal)}
.email{position:absolute;left:620px;top:4358px;width:286px;height:46px;border:1.5px solid #86dbe3;border-radius:24px;font-size:14px;color:var(--muted);padding-left:37px;display:flex;align-items:center}
.social{position:absolute;left:961px;top:4343px;list-style:none}
.social li{display:flex;align-items:center;gap:14px;font-size:14px;font-weight:600;text-transform:uppercase;height:39px}
.social li span{width:25px;height:25px;border:1.5px solid var(--blue);border-radius:3px}
.f-line{position:absolute;left:94px;top:4522px;width:1012px;height:1px;background:#bfc4c8}
.copy{position:absolute;left:0;top:4533px;width:1200px;text-align:center;font-size:12.5px}
</style>
</head>
<body>

<!-- header -->
<div class="topline"></div>
<div class="brand" style="left:106px;top:40px;font-size:48px"><span>trelvo</span><span class="dot" style="width:16px;height:16px"></span></div>
<nav class="nav"><span>Home</span><span>About</span><span>Products</span><span>Industry Solutions</span><span>Contact</span></nav>
<div class="btn" style="left:929px;top:42px;width:165px;height:43px;font-size:16px">Rent Now</div>

<!-- hero -->
<div class="photo" role="img" aria-label="Outdoor wedding ceremony aisle with a photo-printed hand sanitizer stand in the foreground" style="left:0;top:124px;width:1200px;height:600px;background:linear-gradient(90deg,#5b6a3a 0%,#c8b79a 28%,#d9cdbd 50%,#b4a27f 70%,#e9d9d2 100%)"></div>
<div class="hero-box">
  <h1 class="serif">Welcome Your Guests With Something Truly Unique</h1>
  <div class="btn" style="left:46px;top:246px;width:135px;height:43px">Check Price</div>
</div>
<div class="dots"><span></span><span class="on"></span><span></span><span></span><span></span></div>

<!-- about -->
<h2 class="sec-title serif" style="top:788px">About Us</h2>
<p class="lede" style="top:862px">Contrary to popular belief, Lorem Ipsum is not simply random text. It has roots in a piece of classical Latin literature from 45 BC, making it over 2000 years old. Daniel Ashcombe, a Latin professor at Wrenfield College in Virginia,</p>

<div class="card" style="left:106px">
  <h3><svg width="30" height="34" viewBox="0 0 30 34" fill="none" stroke="#111" stroke-width="2"><path d="M15 32C7 22 4 17 4 12a11 11 0 0122 0c0 5-3 10-11 20z"/><circle cx="15" cy="12" r="4"/></svg>Founded in Europe in 2015</h3>
  <p>2015: first US and international patents filed</p>
  <p>2016: first units manufactured and sold</p>
  <p>2017: additional patents filed and European rollout begun</p>
  <p>2019: recapitalization of business and worldwide rollout</p>
</div>
<div class="card hot" style="left:451px">
  <h3><svg width="32" height="32" viewBox="0 0 32 32" fill="none" stroke="#fff" stroke-width="2"><circle cx="16" cy="16" r="13" stroke-dasharray="4 3"/><circle cx="16" cy="16" r="6"/></svg>Product deployed &amp; in use around the world</h3>
  <p>Thousands of hours of continued development and improvement in 2018 and 2019</p>
  <p>Over 2000 sold worldwide to date</p>
  <p>North American business established in 2020 as Trelvo LLC</p>
</div>
<div class="card" style="left:795px">
  <h3><svg width="28" height="32" viewBox="0 0 28 32" fill="none" stroke="#111" stroke-width="2"><path d="M14 2l11 4v9c0 8-5 13-11 15C8 28 3 23 3 15V6z"/><circle cx="14" cy="15" r="4"/></svg>Protected by five international patents</h3>
  <p>Patented collecting tray that prevents spills and mess</p>
  <p>Patented dispenser that works reliably, consistently, and accurately</p>
  <p>Design patents filed to protect form and structure of device</p>
</div>

<!-- features -->
<div class="features" role="img" aria-label="Faint overhead view of a wedding banquet table with plates and dishes"></div>
<h2 class="sec-title serif" style="top:1381px">Our Features</h2>
<div class="feat-img" role="img" aria-label="Hand sanitizer stand printed with a wedding couple photo"></div>

<div class="feat l" style="right:634px;top:1469px">Tracks And Reports Behavior<span class="ico"><svg width="20" height="20" fill="none" stroke="#fff" stroke-width="2"><circle cx="6" cy="6" r="3"/><circle cx="14" cy="14" r="3"/><path d="M8 8l4 4"/></svg></span></div>
<div class="feat l" style="right:697px;top:1554px">Wireless Connection<span class="ico"><svg width="20" height="20" fill="none" stroke="#fff" stroke-width="2"><path d="M3 8a10 10 0 0114 0M6 11a6 6 0 018 0"/><circle cx="10" cy="15" r="1.5"/></svg></span></div>
<div class="feat l" style="right:736px;top:1639px">Virus-induced Shutdown<span class="ico"><svg width="20" height="20" fill="none" stroke="#fff" stroke-width="2"><circle cx="10" cy="10" r="4"/><path d="M10 2v4M10 14v4M2 10h4M14 10h4"/></svg></span></div>
<div class="feat l" style="right:742px;top:1738px">Customize Your Sanitizer With<br>Any Photo, Any Size, Any Shape<span class="ico"><svg width="20" height="20" fill="none" stroke="#fff" stroke-width="2"><rect x="3" y="3" width="14" height="14" rx="2"/><path d="M3 14l5-5 4 4 2-2 3 3"/></svg></span></div>
<div class="feat l" style="right:678px;top:1827px">Predict Busy Periods<span class="ico"><svg width="20" height="20" fill="none" stroke="#fff" stroke-width="2"><circle cx="5" cy="7" r="2"/><circle cx="10" cy="7" r="2"/><circle cx="15" cy="7" r="2"/><path d="M2 16c1-3 15-3 16 0"/></svg></span></div>

<div class="feat" style="left:637px;top:1469px"><span class="ico"><svg width="20" height="20" fill="none" stroke="#fff" stroke-width="2"><path d="M17 3L3 9l6 2 2 6z"/></svg></span>Locate Them Anywhere</div>
<div class="feat" style="left:697px;top:1554px"><span class="ico"><svg width="20" height="20" fill="none" stroke="#fff" stroke-width="2"><path d="M4 16l12-12M7 6l7 7"/></svg></span>No Plugs Or Wires</div>
<div class="feat" style="left:729px;top:1639px"><span class="ico"><svg width="20" height="20" fill="none" stroke="#fff" stroke-width="2"><rect x="6" y="3" width="8" height="15" rx="1"/><path d="M9 1h2"/></svg></span>Long Battery Life</div>
<div class="feat" style="left:742px;top:1738px"><span class="ico"><svg width="20" height="20" fill="none" stroke="#fff" stroke-width="2"><rect x="3" y="7" width="8" height="8" rx="2"/><rect x="9" y="4" width="8" height="8" rx="2"/></svg></span>Durable</div>
<div class="feat" style="left:680px;top:1827px"><span class="ico"><svg width="20" height="20" fill="none" stroke="#fff" stroke-width="2"><path d="M4 16L14 6M11 3l6 6"/></svg></span>Easily Customizable</div>

<!-- services -->
<h2 class="sec-title serif" style="top:1935px">Our Services</h2>
<p class="lede" style="top:2009px">Contrary to popular belief, Lorem Ipsum is not simply random text. It has roots in a piece of classical Latin literature from 45 BC, making it over 2000 years old. Daniel Ashcombe, a Latin professor at Wrenfield College in Virginia,</p>

<div class="row-bg" style="top:2122px"></div>
<div class="photo" role="img" aria-label="Sanitizer stand with couple photo in a blurred wedding venue" style="left:0;top:2122px;width:600px;height:526px;background:linear-gradient(135deg,#7a5a46,#b59a86 50%,#6d5748)"></div>
<div class="svc" style="left:469px;top:2200px;height:370px">
  <h2>Welcome your guests with something truly unique – a customized hand sanitizer</h2>
  <p>Why have a generic, industrial hand sanitizer when you could have something truly unique and different?</p>
  <ul>
    <li>Customize the photo above the spout and the spout decoration</li>
    <li>Choose any size and shape photo you wish</li>
    <li>Choose from our standard spout decorations or design one of your own. We'll take care of producing and fitting it.</li>
  </ul>
  <span class="btn">Check price and availability</span>
</div>

<div class="row-bg" style="top:2648px"></div>
<div class="photo" role="img" aria-label="Sanitizer stand with couple photo beside a garden wedding arch" style="left:600px;top:2648px;width:600px;height:524px;background:linear-gradient(135deg,#4f6a3a,#9aa58a 45%,#c9c4bc)"></div>
<div class="svc" style="left:106px;top:2742px;height:336px">
  <h2>Customize your sanitizer with any photo,<br>any size, any shape</h2>
  <ul>
    <li>Choose a photo of the happy couple, the proud parents, or anything else you wish</li>
    <li>Choose any size or shape you wish, up to 24x36"</li>
    <li>We take care of all production and customization</li>
  </ul>
  <span class="btn">Check price and availability</span>
</div>

<div class="row-bg" style="top:3172px"></div>
<div class="photo" role="img" aria-label="Sanitizer stand with couple photo and wedding cake spout in a floral setting" style="left:0;top:3172px;width:600px;height:524px;background:linear-gradient(135deg,#5f7048,#cfc6bd 50%,#8e8a7c)"></div>
<div class="svc" style="left:469px;top:3269px;height:331px">
  <h2>Choose one of our standard spouts, or design your own</h2>
  <ul>
    <li>Choose one of our standard spouts - wedding cake, flower vase, or "just married" car. More spout decorations will be added each month</li>
    <li>For an additional fee, our team of 3D designers will design, 3D print, and decorate a spout just for your event</li>
  </ul>
  <span class="btn">Check price and availability</span>
</div>

<div class="row-bg" style="top:3696px"></div>
<div class="photo" role="img" aria-label="Wedding reception decor with white arch and a sanitizer stand" style="left:600px;top:3696px;width:600px;height:525px;background:linear-gradient(135deg,#d8cdc4,#efe9e3 50%,#c9b9ad)"></div>
<div class="svc" style="left:106px;top:3791px;height:337px">
  <h2 style="margin-top:28px">Greet your guests with an act of care</h2>
  <ul>
    <li>Make your friends and family feel welcome and safe with a rugged, durable hand sanitizer from Trelvo</li>
    <li>Our battery-powered dispensers are reliable, wireless, and touchless</li>
    <li>Filled with your choice from our wide range of sanitizing products</li>
  </ul>
  <span class="btn">Check price and availability</span>
</div>

<!-- footer -->
<div class="brand" style="left:106px;top:4340px;font-size:62px"><span>trelvo</span><span class="dot" style="width:20px;height:20px"></span></div>
<div class="f-head serif" style="left:421px">Site Map</div>
<ul class="sitemap"><li>Home</li><li>About us</li><li>Products</li><li>Industry Solutions</li><li>Contact Us</li></ul>
<div class="f-head serif" style="left:620px">Email Subscribe</div>
<div class="email">Email Address</div>
<div class="btn" style="left:620px;top:4420px;width:286px;height:38px;font-size:14px">Subscribe Now</div>
<div class="f-head serif" style="left:961px">Follow Us</div>
<ul class="social"><li><span></span>Friendbook</li><li><span></span>Circle Plus</li><li><span></span>Work Link</li><li><span></span>Snapgram</li></ul>
<div class="f-line"></div>
<div class="copy">Copyright © 2021 Trelvo. All rights reserved.</div>

</body>
</html>
```